Flyer für Betreuungsleistungen und Verhinderungspflege erstellen
Zielgruppe
wir sind ein mobiler Pflegedienst in Rostock und versorgen Patienten in der Häuslichkeit.
Aufgabenstellung
Es soll ein Flyer erstellt werde mit folgendem Text:
5 Weitere Punkte folgen noch. Der Flyer soll seriös und exklusiv wirken.
Unsere Betreuungsangebote
Wenn Sie eine Pflegestufe haben, können Sie auf verschiedene Angebote der Betreuung Nutzen.
Betreuungsleistungen und die Leistungen der Verhinderungspflege sollen für Pflegebedürftige unter anderem aktivierende und qualitätsgesicherte Betreuungsangebote verfügbar machen und pflegenden Angehörigen eine Möglichkeit der Entlastung bieten.
Die Leistungen können auch von Patienten in Anspruch genommen werden, die Pflegegeld in Anspruch nehmen und sich nicht der Hilfe eines Pflegedienstes bedienen. Das Budget wird zusätzlich zum Pflegegeld zur Verfügung gestellt.
Bewegung:
Da pflegebedürftige Menschen zu sozialem Rückzug und zur körperlichen Versteifung neigen, sind körperliche Aktivitäten wie Bewegungsspiele und eine kontinuierliche uns konsequente Anleitung zur Mobilität besonders wichtig. Dabei hilft nicht nur, mobil zu bleiben und Energie zu lenken. Da Wahrnehmung und Bewegung voneinander Unabhängig sind, fördert Bewegung die Wahrnehmung sowie den Kontakt zur Umwelt und vermindert damit Anspannung, Ängste und Aggressionen.
_ 5 weitere Punkte folgen noch---

```html
<!DOCTYPE html>
<html lang="de">
<head>
<meta charset="utf-8">
<title>Flyer Betreuungsangebote – Pflegedienst Küstenlicht</title>
<link rel="stylesheet" href="https://fonts.googleapis.com/css2?family=Quicksand:wght@300;400;700&family=Nunito+Sans:wght@400&display=swap">
<style>
:root{
  --green:#5fb336;
  --blue:#0a52a0;
  --orange:#f08424;
  --ink:#1c4f9c;
  --white:#ffffff;
  --photo-warm-a:#e8c9a6;
  --photo-warm-b:#b7a98a;
  --photo-green-a:#6f8f55;
  --photo-green-b:#c9b8a5;
  --photo-hand-a:#f7d98a;
  --photo-hand-b:#e59f6b;
  --photo-care-a:#f4f4f2;
  --photo-care-b:#4d8fb0;
}
*{margin:0;padding:0;box-sizing:border-box}
html,body{width:1200px;height:1200px;overflow:hidden;background:var(--white)}
body{position:relative;font-family:"Nunito Sans",sans-serif;color:var(--ink)}
.panel{position:absolute;background:var(--white);overflow:hidden;box-shadow:2px 3px 8px rgba(0,0,0,.28)}
.panel svg.bands{position:absolute;left:0;top:0}
.t{position:absolute;font-family:"Quicksand",sans-serif;font-weight:400;line-height:1.15}
.head-white{color:var(--white)}
.head-blue{color:var(--ink)}
.body{position:absolute;font-family:"Nunito Sans",sans-serif;line-height:1.38}
.body p+p{margin-top:.9em}
.on-green{color:var(--white)}
.list{position:absolute;text-align:center;font-family:"Quicksand",sans-serif;font-weight:400;color:var(--ink)}
.list li{list-style:none;position:absolute;left:0;right:0}
.brand{position:absolute;display:flex;flex-direction:column;align-items:center}
.brand .dot{border-radius:50%;background:var(--green)}
.brand .name{font-family:"Nunito Sans",sans-serif;font-weight:400;color:var(--ink);text-align:center;line-height:1.1}
.contact{position:absolute;color:var(--white);font-family:"Nunito Sans",sans-serif;line-height:1.32}
.url{position:absolute;color:var(--white);font-family:"Quicksand",sans-serif;font-weight:400}
.caption{position:absolute;font-family:"Quicksand",sans-serif;font-weight:700;color:#111;font-size:24px;transform:translateX(-50%)}

.outside{left:33px;top:16px;width:558px;height:397px}
.inside-spread{left:619px;top:17px;width:553px;height:394px}
.cover{left:33px;top:499px;width:298px;height:635px}
.inside-open{left:396px;top:544px;width:445px;height:481px}
.back{left:882px;top:494px;width:294px;height:639px}
</style>
</head>
<body>

<section class="panel outside" aria-label="Außenseite">
  <svg class="bands" width="558" height="397" viewBox="0 0 558 397">
    <defs>
      <linearGradient id="o1" x1="0" x2="1" y1="0" y2="1"><stop offset="0" stop-color="var(--photo-green-a)"/><stop offset="1" stop-color="var(--photo-green-b)"/></linearGradient>
      <linearGradient id="o2" x1="0" x2="1"><stop offset="0" stop-color="var(--photo-hand-a)"/><stop offset="1" stop-color="var(--photo-hand-b)"/></linearGradient>
      <linearGradient id="o3" x1="0" x2="1" y1="0" y2="1"><stop offset="0" stop-color="var(--photo-care-a)"/><stop offset="1" stop-color="var(--photo-care-b)"/></linearGradient>
    </defs>
    <path d="M0,0H558V58C520,82 470,84 420,80C300,70 150,40 0,62Z" fill="var(--green)"/>
    <path role="img" aria-label="Foto: Seniorin und Pflegerin lachen gemeinsam am Laptop" d="M0,232C60,222 130,242 183,240V340H0Z" fill="url(#o1)"/>
    <path role="img" aria-label="Foto: junge Hand hält ältere Hand" d="M183,240C250,236 310,250 370,262V340H183Z" fill="url(#o2)"/>
    <rect role="img" aria-label="Foto: lächelnde Pflegerin mit älterer Patientin" x="370" y="172" width="188" height="168" fill="url(#o3)"/>
    <path d="M0,330C150,318 300,322 400,316C480,312 530,302 558,290V397H0Z" fill="var(--orange)"/>
    <path d="M0,346C150,338 300,344 400,340C480,338 530,332 558,324V397H0Z" fill="var(--blue)"/>
  </svg>
  <div class="t head-white" style="left:61px;top:16px;font-size:12px">Bewegung</div>
  <div class="t head-white" style="left:372px;top:18px;width:186px;text-align:center;font-size:18px;font-weight:300">Hier steht<br>Ihre Headline</div>
  <div class="body head-blue" style="left:22px;top:86px;width:142px;font-size:6.6px">Da pflegebedürftige Menschen zu sozialem Rückzug und zur körperlichen Versteifung neigen, sind körperliche Aktivitäten wie Bewegungsspiele und eine kontinuierliche uns konsequente Anleitung zur Mobilität besonders wichtig. Dabei hilft nicht nur, mobil zu bleiben und Energie zu lenken. Da Wahrnehmung und Bewegung voneinander Unabhängig sind, fördert Bewegung die Wahrnehmung sowie den Kontakt zur Umwelt und vermindert damit Anspannung, Ängste und Aggressionen.</div>
  <ul class="list" style="left:200px;top:0;width:155px;font-size:14px">
    <li style="top:72px">Bewegung</li>
    <li style="top:106px">Betreuung</li>
    <li style="top:142px">Punkt 1</li>
    <li style="top:170px">Punkt 2</li>
    <li style="top:196px">Punkt 3</li>
  </ul>
  <div class="brand" style="left:400px;top:94px;width:130px">
    <span class="dot" style="width:44px;height:44px"></span>
    <span class="name" style="font-size:10px;margin-top:6px">Pflegedienst<br>Küstenlicht</span>
  </div>
  <div class="contact" style="left:202px;top:351px;font-size:6.6px">Pflegedienst Küstenlicht<br>Hafenweg 12 • 18055 Rostock<br>Tel: 0800 12345 67<br>info@pflegedienst-kuestenlicht.de</div>
  <div class="url" style="left:372px;top:370px;width:186px;text-align:center;font-size:9.5px">pflegedienst-kuestenlicht.de</div>
</section>
<div class="caption" style="left:139px;top:433px">aussen</div>

<section class="panel inside-spread" aria-label="Innenseite">
  <svg class="bands" width="553" height="394" viewBox="0 0 553 394">
    <path d="M0,68C90,76 160,74 230,56C280,42 320,34 380,38C450,42 510,58 553,67V394H0Z" fill="var(--green)"/>
    <path d="M0,351C90,356 200,344 287,323C380,306 480,318 553,332V394H0Z" fill="var(--orange)"/>
    <path d="M0,360C90,362 200,352 287,338C380,326 480,338 553,352V394H0Z" fill="var(--blue)"/>
  </svg>
  <div class="t head-blue" style="left:0;top:18px;width:184px;text-align:center;font-size:12px">Betreuungsangebote</div>
  <div class="t head-blue" style="left:184px;top:18px;width:184px;text-align:center;font-size:12px">Punkt 2</div>
  <div class="t head-blue" style="left:368px;top:18px;width:184px;text-align:center;font-size:12px">Punkt 3</div>
  <div class="body on-green" style="left:19px;top:125px;width:150px;font-size:6.5px">
    <p>Wenn Sie eine Pflegestufe haben, können Sie auf verschiedene Angebote der Betreuung Nutzen.</p>
    <p>Betreuungsleistungen und die Leistungen der Verhinderungspflege sollen für Pflege­bedürftige unter anderem aktivierende und qualitätsgesicherte Betreuungsangebote ver­fügbar machen und pflegenden Angehörigen eine Möglichkeit der Entlastung bieten.</p>
    <p>Die Leistungen können auch von Patienten in Anspruch genommen werden, die Pflegegeld in Anspruch nehmen und sich nicht der Hilfe eines Pflegedienstes bedienen. Das Budget wird zusätzlich zum Pflegegeld zur Verfügung gestellt.</p>
  </div>
  <div class="body on-green" style="left:204px;top:125px;width:150px;font-size:6.5px">
    <p>Wenn Sie eine Pflegestufe haben, können Sie auf verschiedene Angebote der Betreuung Nutzen.</p>
    <p>Betreuungsleistungen und die Leistungen der Verhinderungspflege sollen für Pflege­bedürftige unter anderem aktivierende und qualitätsgesicherte Betreuungsangebote ver­fügbar machen und pflegenden Angehörigen eine Möglichkeit der Entlastung bieten.</p>
    <p>Die Leistungen können auch von Patienten in Anspruch genommen werden, die Pflegegeld in Anspruch nehmen und sich nicht der Hilfe eines Pflegedienstes bedienen. Das Budget wird zusätzlich zum Pflegegeld zur Verfügung gestellt.</p>
  </div>
  <div class="body on-green" style="left:389px;top:125px;width:150px;font-size:6.5px">
    <p>Wenn Sie eine Pflegestufe haben, können Sie auf verschiedene Angebote der Betreuung Nutzen.</p>
    <p>Betreuungsleistungen und die Leistungen der Verhinderungspflege sollen für Pflege­bedürftige unter anderem aktivierende und qualitätsgesicherte Betreuungsangebote ver­fügbar machen und pflegenden Angehörigen eine Möglichkeit der Entlastung bieten.</p>
    <p>Die Leistungen können auch von Patienten in Anspruch genommen werden, die Pflegegeld in Anspruch nehmen und sich nicht der Hilfe eines Pflegedienstes bedienen. Das Budget wird zusätzlich zum Pflegegeld zur Verfügung gestellt.</p>
  </div>
  <div class="url" style="left:0;top:366px;width:553px;text-align:center;font-size:12px">Spruch spruch spruch</div>
</section>
<div class="caption" style="left:906px;top:433px">innen</div>

<section class="panel cover" aria-label="Titelseite">
  <svg class="bands" width="298" height="635" viewBox="0 0 298 635">
    <defs>
      <linearGradient id="c1" x1="0" x2="1" y1="0" y2="1"><stop offset="0" stop-color="var(--photo-care-a)"/><stop offset="1" stop-color="var(--photo-care-b)"/></linearGradient>
    </defs>
    <path d="M0,0H298V92C250,118 200,130 150,129C90,128 40,116 0,114Z" fill="var(--green)"/>
    <rect role="img" aria-label="Foto: lächelnde Pflegerin mit älterer Patientin" x="0" y="282" width="298" height="280" fill="url(#c1)"/>
    <path d="M0,539C80,548 180,540 240,512C265,500 285,490 298,482V635H0Z" fill="var(--orange)"/>
    <path d="M0,573C80,585 180,584 240,565C265,556 285,548 298,542V635H0Z" fill="var(--blue)"/>
  </svg>
  <div class="t head-white" style="left:0;top:28px;width:298px;text-align:center;font-size:29px;font-weight:300;line-height:1.2">Hier steht<br>Ihre Headline</div>
  <div class="brand" style="left:49px;top:150px;width:200px">
    <span class="dot" style="width:80px;height:80px"></span>
    <span class="name" style="font-size:18px;margin-top:12px">Pflegedienst<br>Küstenlicht</span>
  </div>
  <div class="url" style="left:0;top:594px;width:298px;text-align:center;font-size:17px">pflegedienst-kuestenlicht.de</div>
</section>
<div class="caption" style="left:177px;top:1152px">Titel</div>

<section class="panel inside-open" aria-label="Innenseite aufgeklappt">
  <svg class="bands" width="445" height="481" viewBox="0 0 445 481">
    <defs>
      <linearGradient id="i1" x1="0" x2="1" y1="0" y2="1"><stop offset="0" stop-color="var(--photo-green-a)"/><stop offset="1" stop-color="var(--photo-green-b)"/></linearGradient>
    </defs>
    <path d="M0,86C80,88 160,86 222,78V481H0Z" fill="var(--green)"/>
    <path d="M222,0H445V46C360,50 290,62 222,75Z" fill="var(--green)"/>
    <path role="img" aria-label="Foto: Seniorin und Pflegerin lachen gemeinsam am Laptop" d="M222,318C290,300 370,292 445,294V420H222Z" fill="url(#i1)"/>
    <path d="M0,428C100,446 250,408 445,400V481H0Z" fill="var(--orange)"/>
    <path d="M0,446C100,460 250,424 445,416V481H0Z" fill="var(--blue)"/>
    <line x1="222.5" y1="0" x2="222.5" y2="481" stroke="rgba(0,0,0,.12)" stroke-width="1"/>
  </svg>
  <div class="t head-blue" style="left:0;top:22px;width:222px;text-align:center;font-size:15px">Betreuungsangebote</div>
  <div class="t head-white" style="left:222px;top:14px;width:223px;text-align:center;font-size:15px">Bewegung</div>
  <div class="body on-green" style="left:23px;top:155px;width:180px;font-size:8.5px">
    <p>Wenn Sie eine Pflegestufe haben, können Sie auf verschiedene Angebote der Betreuung Nutzen.</p>
    <p>Betreuungsleistungen und die Leistungen der Verhinderungspflege sollen für Pflege­bedürftige unter anderem aktivierende und qualitätsgesicherte Betreuungsangebote ver­fügbar machen und pflegenden Angehörigen eine Möglichkeit der Entlastung bieten.</p>
    <p>Die Leistungen können auch von Patienten in Anspruch genommen werden, die Pflegegeld in Anspruch nehmen und sich nicht der Hilfe eines Pflegedienstes bedienen. Das Budget wird zusätzlich zum Pflegegeld zur Verfügung gestellt.</p>
  </div>
  <div class="body head-blue" style="left:247px;top:102px;width:172px;font-size:8.5px">Da pflegebedürftige Menschen zu sozialem Rückzug und zur körperlichen Versteifung neigen, sind körperliche Aktivitäten wie Bewegungsspiele und eine kontinuierliche uns konsequente Anleitung zur Mobilität besonders wichtig. Dabei hilft nicht nur, mobil zu bleiben und Energie zu lenken. Da Wahrnehmung und Bewegung voneinander Unabhängig sind, fördert Bewegung die Wahrnehmung sowie den Kontakt zur Umwelt und vermindert damit Anspannung, Ängste und Aggressionen.</div>
</section>
<div class="caption" style="left:588px;top:1038px">innen</div>

<section class="panel back" aria-label="Rückseite">
  <svg class="bands" width="294" height="639" viewBox="0 0 294 639">
    <defs>
      <linearGradient id="b1" x1="0" x2="1" y1="0" y2="1"><stop offset="0" stop-color="var(--photo-hand-a)"/><stop offset="1" stop-color="var(--photo-hand-b)"/></linearGradient>
    </defs>
    <path d="M0,0H294V110C220,92 120,62 0,56Z" fill="var(--green)"/>
    <path role="img" aria-label="Foto: junge Hand hält ältere Hand" d="M0,372C100,380 200,400 294,422V560H0Z" fill="url(#b1)"/>
    <path d="M0,516C100,524 200,530 294,544V639H0Z" fill="var(--orange)"/>
    <path d="M0,531C100,540 200,548 294,562V639H0Z" fill="var(--blue)"/>
  </svg>
  <ul class="list" style="left:0;top:0;width:294px;font-size:22px">
    <li style="top:116px">Bewegung</li>
    <li style="top:171px">Betreuung</li>
    <li style="top:228px">Punkt 1</li>
    <li style="top:274px">Punkt 2</li>
    <li style="top:316px">Punkt 3</li>
  </ul>
  <div class="contact" style="left:23px;top:564px;font-size:11.5px">Pflegedienst Küstenlicht<br>Hafenweg 12 • 18055 Rostock<br>Tel: 0800 12345 67<br>info@pflegedienst-kuestenlicht.de</div>
</section>
<div class="caption" style="left:1055px;top:1152px">Rückseite</div>

</body>
</html>
```